依頼詳細
❏デザイン依頼
・ロゴ色/マゼンタ
・親近感・高級感・心からリラックスできる空間

☆リッチメニューのデザインの狙い
タ−ゲット層に高級感のある落ち着きでリラックスしていただける空間を提供していきたい。
そして、お客様の内面、外面のケアを安心して任せれる信頼感をつくる。

❏依頼詳細
<作成物>
■リッチメッセージ
リッチメニュー
合計2枚

〈リッチメニューの項目〉
下の段左から右へ①〜③
下の段左から右へ④〜⑤

〈リッチメニューの表示名〉
①About us   ②お店情報     ③SNS/Blog
④オンラインショップ ⑤最新情報 ⑥予約・問合せ

デザイン重視でここの表示名はデザイン的に英語の方がよければ
英語でも大丈夫です。意味がわかって
ニュアンスがあっていれば文字を短くするのも
お任せします。あくまでデザイン重視です。

〈画像はこちらから〉
↓ギガファイルリンク
https://52.sorahako-okuru.net/0925-a83c19b07d5e2f416c88a0b3d95e1c27

※こちらの作成以外に勝手に使用された場合は
著作権侵害で法的手段をとらせていただきます。
作成事例にも使用しないでください。

<サイズ>
・リッチメッセージ(1040×1040ピクセル)
・リッチメニュー(1200×810ピクセル)

<納品形式>
・ai形式(イラストレーターデータ)
・JPG
<詳細>
※添付ファイルをご確認ください。

<備考>
納品前の修正について、回数制限などありますか?
納品後の修正について、回数制限や料金などを教えて下さい。
色々なデザインでのご応募をお待ちしております!
記載項目
・元氣と綺麗になれるイメージ
・トータルビューティ−で内面から素敵な人に
サイズ
• ・リッチメッセージ(1040×1040ピクセル) ・リッチメニュー(1200×810ピクセル)
希望イメージ
シンプル 複雑
単色 カラフル
暗い 明るい
日常 高級
遊び心 厳粛
未来的 伝統的
女性的 男性的
希望する色
赤系、マゼンダ
納品ファイル
• 高解像度JPG (.jpg)
• イラストレーター形式 (.ai)
補足説明

依頼内容にぴったりで、対応も素晴らしかった。

様々な素敵な提案をありがとうございました。
今後も宜しくお願いします。

```html
<!DOCTYPE html>
<html lang="ja">
<head>
<meta charset="utf-8">
<title>Lune Rich Menu</title>
<link href="https://fonts.googleapis.com/css2?family=Noto+Serif+JP:wght@400;600&family=Noto+Sans+JP:wght@400;500&display=swap" rel="stylesheet">
<style>
  :root {
    --magenta: #9a2a57;
    --magenta-deep: #7e1f45;
    --magenta-soft: #b8587f;
    --blush: #f3dde5;
    --blush-deep: #e3bccb;
    --white: #ffffff;
    --photo-warm: #c9a58a;
    --photo-wood: #b98a62;
    --interior: #e9ddd3;
  }
  * { margin: 0; padding: 0; box-sizing: border-box; }
  html, body { width: 777px; height: 1200px; overflow: hidden; background: var(--white); }
  .menu { position: relative; width: 777px; height: 1200px; overflow: hidden; font-family: "Noto Serif JP", serif; }
  .staff-photo {
    position: absolute; left: 0; top: 0; width: 777px; height: 380px;
    background: linear-gradient(180deg, var(--photo-wood) 0%, var(--photo-warm) 60%, #d9c3b3 100%);
  }
  .interior-band {
    position: absolute; left: 0; top: 440px; width: 777px; height: 160px;
    background: linear-gradient(90deg, #d7c6b6 0%, var(--interior) 45%, #f1e8e2 100%);
  }
  .arc { position: absolute; left: 0; top: 360px; width: 777px; height: 110px; }
  .logo-card {
    position: absolute; left: 236px; top: 315px; width: 305px; height: 290px;
    background: var(--white);
    clip-path: polygon(16% 0, 84% 0, 100% 50%, 84% 100%, 16% 100%, 0 50%);
    display: flex; flex-direction: column; align-items: center; justify-content: center;
    color: var(--magenta);
  }
  .logo-card .tagline-en { font-family: "Noto Sans JP", sans-serif; font-size: 13px; letter-spacing: 1px; }
  .logo-card .brand { font-size: 84px; font-weight: 600; line-height: 1.1; color: var(--magenta); }
  .logo-card .brand-sub { font-family: "Noto Sans JP", sans-serif; font-size: 12px; letter-spacing: 2px; }
  .catch-band {
    position: absolute; left: 0; top: 596px; width: 777px; height: 54px;
    background: var(--magenta);
    color: var(--white); font-size: 30px; text-align: center; line-height: 54px; letter-spacing: 1px;
  }
  .menu-area {
    position: absolute; left: 0; top: 650px; width: 777px; height: 550px;
    background: var(--magenta);
  }
  .floral-area {
    position: absolute; left: 0; top: 930px; width: 777px; height: 270px;
    background: linear-gradient(180deg, var(--magenta) 0%, var(--blush-deep) 40%, var(--blush) 100%);
  }
  .tiles { position: absolute; left: 0; top: 650px; width: 777px; height: 550px; }
  .tile-label {
    position: absolute; width: 200px; text-align: center;
    color: var(--white); font-family: "Noto Sans JP", sans-serif; font-size: 25px; line-height: 1.3;
    transform: translate(-50%, -50%);
  }
</style>
</head>
<body>
<main class="menu">
  <div class="staff-photo" role="img" aria-label="Five smiling salon staff members standing together against a wooden wall"></div>
  <div class="interior-band" role="img" aria-label="Bright salon interior with plants and styling chairs"></div>
  <svg class="arc" viewBox="0 0 777 110" preserveAspectRatio="none" aria-hidden="true">
    <path d="M0 20 Q388 110 777 20 L777 0 L0 0 Z" fill="var(--white)"/>
    <path d="M0 20 Q388 110 777 20 L777 60 Q388 140 0 60 Z" fill="var(--magenta)"/>
  </svg>
  <div class="logo-card">
    <div class="tagline-en">Hair / Relaxation</div>
    <div class="brand">Lune</div>
    <div class="brand-sub">total beauty salon</div>
  </div>
  <div class="catch-band">トータルビューティーで内面から素敵な人に</div>
  <div class="menu-area"></div>
  <div class="floral-area" role="img" aria-label="Soft pink floral pattern"></div>
  <svg class="tiles" viewBox="0 0 777 550" aria-hidden="true">
    <g stroke="var(--white)" stroke-width="3">
      <polygon points="142,50 245,153 142,256 39,153" fill="var(--magenta-soft)"/>
      <polygon points="389,50 492,153 389,256 286,153" fill="var(--magenta-soft)"/>
      <polygon points="635,50 738,153 635,256 532,153" fill="var(--magenta-soft)"/>
      <polygon points="142,296 245,399 142,502 39,399" fill="var(--magenta-soft)"/>
      <polygon points="389,296 492,399 389,502 286,399" fill="var(--magenta-soft)"/>
      <polygon points="635,296 738,399 635,502 532,399" fill="var(--magenta-soft)"/>
    </g>
  </svg>
  <div class="tile-label" style="left:142px;top:803px">About us</div>
  <div class="tile-label" style="left:389px;top:803px">お店情報</div>
  <div class="tile-label" style="left:635px;top:803px">SNS/Blog</div>
  <div class="tile-label" style="left:142px;top:1049px">オンライン<br>ショップ</div>
  <div class="tile-label" style="left:389px;top:1049px">最新情報</div>
  <div class="tile-label" style="left:635px;top:1049px">予約・問合せ</div>
</main>
</body>
</html>
```